Improvement of design for elearning template

Our company provides web based elearning courses for employees. We have a design layout for the different slides which can be found here: https://www.filecrate-share.example/s/qk7tr2mplx9e/BXnTpWvZrKdMeYfLs4QjHcUa?view=1. The content will be added later. At this point we are just looking for a design layout that works with different content types like images, text, quiz & videos. What we would ask you, is to pick randomly 1 or 2 of the elearning slides from the existing designs and suggest improvements or come up with an alternative design. The winner of the design project can work on all slides and this will be a project with a much larger budget.
Target Market(s)
Employees in large enterprises
Look and feel
Each slider illustrates characteristics of the customer's brand and the style your logo design should communicate.

```html
<!DOCTYPE html>
<html lang="en">
<head>
<meta charset="utf-8">
<title>Lesson Overview</title>
<link rel="stylesheet" href="https://fonts.googleapis.com/css2?family=Quicksand:wght@400;500;600;700&display=swap">
<style>
  :root {
    --brand: #2f5fad;
    --brand-dark: #2a58a6;
    --ink: #3a3f4a;
    --bg: #ffffff;
    --blob: #dde7f9;
    --blob-light: #edf3fd;
    --card-top: #ffffff;
    --card-bottom: #d8e4f8;
    --card-border: #b5b9c2;
    --art-top: #a9c6f5;
    --art-bottom: #78a8f1;
    --track: #ffffff;
    --dots: #e9effb;
  }
  * { box-sizing: border-box; margin: 0; padding: 0; }
  html, body { width: 1200px; height: 619px; overflow: hidden; background: var(--bg); }
  body { font-family: "Quicksand", sans-serif; color: var(--brand); }
  .slide { position: relative; width: 1200px; height: 619px; overflow: hidden; }
  .backdrop { position: absolute; inset: 0; }

  .brand { position: absolute; left: 58px; top: 37px; display: flex; align-items: center; gap: 10px; }
  .brand-dot { width: 30px; height: 30px; border-radius: 50%; background: var(--brand); }
  .brand-name { font-size: 24px; font-weight: 500; letter-spacing: 0.2px; color: var(--brand); }

  .pill {
    position: absolute; display: flex; align-items: center; justify-content: center; gap: 8px;
    background: var(--brand-dark); color: #fff; border-radius: 16px;
    font-size: 17px; font-weight: 600;
  }
  .pill-home { left: 1033px; top: 44px; width: 74px; height: 28px; }
  .pill-back { left: 988px; top: 553px; width: 80px; height: 28px; }
  .pill-next { left: 1080px; top: 553px; width: 79px; height: 28px; }
  .arrow { width: 0; height: 0; border-top: 5px solid transparent; border-bottom: 5px solid transparent; }
  .arrow-left { border-right: 8px solid #fff; }
  .arrow-right { border-left: 8px solid #fff; }

  .intro { position: absolute; left: 147px; top: 108px; width: 920px; }
  .intro-title { font-size: 27px; font-weight: 700; line-height: 34px; color: var(--brand); }
  .intro-rule { width: 107px; height: 3px; background: var(--brand); margin-top: 1px; }
  .intro-text { margin-top: 10px; font-size: 17px; font-weight: 400; line-height: 21px; color: var(--ink); }

  .lesson-grid {
    position: absolute; left: 243px; top: 238px;
    display: grid; grid-template-columns: repeat(4, 143px); grid-auto-rows: 110px;
    column-gap: 47.5px; row-gap: 55px;
  }
  .lesson-card {
    position: relative; border: 2px solid var(--card-border); border-radius: 12px; overflow: hidden;
    background: linear-gradient(to bottom, var(--card-top) 10%, var(--card-bottom) 55%);
    box-shadow: 0 1px 3px rgba(60, 80, 120, 0.18);
  }
  .lesson-title {
    position: absolute; top: 24px; left: 0; right: 0; padding-left: 16px; text-align: center;
    font-size: 19px; font-weight: 700; letter-spacing: 0.3px; color: var(--brand);
  }
  .lesson-art {
    position: absolute; left: 0; right: 0; bottom: 0; height: 60px;
    background: linear-gradient(to bottom, rgba(169,198,245,0) 0%, var(--art-top) 40%, var(--art-bottom) 100%);
  }

  .dot-field { position: absolute; left: 80px; top: 456px; width: 90px; height: 75px; background: var(--dots); opacity: 0.7; }

  .progress { position: absolute; left: 56px; top: 567px; width: 335px; height: 14px; }
  .progress-track { position: absolute; left: 6px; right: 0; top: 3px; height: 7px; background: var(--track); border-radius: 4px; }
  .progress-fill { position: absolute; left: 6px; top: 3px; width: 166px; height: 7px; background: var(--brand-dark); border-radius: 4px 0 0 4px; }
  .progress-knob { position: absolute; left: 0; top: 0; width: 14px; height: 14px; border-radius: 50%; background: var(--brand-dark); }
  .progress-label { position: absolute; left: 415px; top: 561px; font-size: 18px; font-weight: 600; color: var(--brand); white-space: nowrap; }
  .progress-label .sep { margin: 0 12px; }
</style>
</head>
<body>
<main class="slide">
  <svg class="backdrop" width="1200" height="619" viewBox="0 0 1200 619" aria-hidden="true">
    <path d="M480 0 C330 70 220 180 150 330 C95 440 40 500 0 520 L0 619 L1200 619 L1200 0 Z" fill="var(--blob)"/>
    <path d="M855 0 C862 60 850 140 900 200 C960 260 1060 300 1200 268 L1200 0 Z" fill="var(--blob-light)"/>
    <path d="M1200 375 C1120 372 1090 400 1040 450 C980 510 920 545 800 552 C700 556 620 580 560 619 L1200 619 Z" fill="#ffffff"/>
  </svg>

  <header class="brand">
    <span class="brand-dot"></span>
    <span class="brand-name">COMPANY NAME</span>
  </header>

  <a class="pill pill-home">Home</a>

  <section class="intro">
    <h1 class="intro-title">What is Lorem Ipsum?</h1>
    <div class="intro-rule"></div>
    <p class="intro-text">Lorem Ipsum is simply dummy text of the printing and typesetting industry. Lorem Ipsum has been the industry's standard dummy text ever since the 1500s</p>
  </section>

  <div class="dot-field" role="img" aria-label="Decorative dot grid"></div>

  <section class="lesson-grid">
    <article class="lesson-card"><div class="lesson-art" role="img" aria-label="Mountain landscape illustration"></div><h2 class="lesson-title">LESSON-1</h2></article>
    <article class="lesson-card"><div class="lesson-art" role="img" aria-label="Mountain landscape illustration"></div><h2 class="lesson-title">LESSON-2</h2></article>
    <article class="lesson-card"><div class="lesson-art" role="img" aria-label="Mountain landscape illustration"></div><h2 class="lesson-title">LESSON-3</h2></article>
    <article class="lesson-card"><div class="lesson-art" role="img" aria-label="Mountain landscape illustration"></div><h2 class="lesson-title">LESSON-4</h2></article>
    <article class="lesson-card"><div class="lesson-art" role="img" aria-label="Mountain landscape illustration"></div><h2 class="lesson-title">LESSON-5</h2></article>
    <article class="lesson-card"><div class="lesson-art" role="img" aria-label="Mountain landscape illustration"></div><h2 class="lesson-title">LESSON-6</h2></article>
    <article class="lesson-card"><div class="lesson-art" role="img" aria-label="Mountain landscape illustration"></div><h2 class="lesson-title">LESSON-7</h2></article>
    <article class="lesson-card"><div class="lesson-art" role="img" aria-label="Mountain landscape illustration"></div><h2 class="lesson-title">LESSON-8</h2></article>
  </section>

  <div class="progress" role="progressbar" aria-valuenow="30" aria-valuemin="0" aria-valuemax="100">
    <div class="progress-track"></div>
    <div class="progress-fill"></div>
    <div class="progress-knob"></div>
  </div>
  <p class="progress-label">Overall Progress 30%<span class="sep">•</span>Lesson 2</p>

  <a class="pill pill-back"><span class="arrow arrow-left"></span>Back</a>
  <a class="pill pill-next">Next<span class="arrow arrow-right"></span></a>
</main>
</body>
</html>
```